I need a wordpress website for myconsulting company specialized in data privacy

I'm looking for a wordpress website for my consulting company specialized in data privacy (GDPR) and computer science.
The website will serve as entry point to for potential clients.
The website should have the following sections (I'm opened to new ideas):
- Presentation of the company
- General presentation
- Services provided with some details
- Blog/articles with tags (if possible)
- Contact
On every page of the website there should be some references to pages (such as privacy policy, legal information...)
If possible he website should be multinlingual (english and french). I'll personnally take care of the translation in french.
Regarding branding;
- Name of the company: Laurent Dubreuil Conseil
- Logo is attached
- For colors to be used see attached PDF for exemple

```html
<!DOCTYPE html>
<html lang="en">
<head>
<meta charset="utf-8">
<title>Laurent Dubreuil Conseil</title>
<link href="https://fonts.googleapis.com/css2?family=Lexend:wght@400;500;600&family=Work+Sans:wght@400;500;600;700&display=swap" rel="stylesheet">
<style>
:root{
  --teal:#0f8a98;
  --teal-dark:#0a6e7a;
  --navy:#0c3350;
  --navy-deep:#0a2a42;
  --ink:#14202b;
  --text:#5d6670;
  --muted:#8a939b;
  --line:#e4e8eb;
  --soft:#f1f4f6;
  --white:#ffffff;
}
*{box-sizing:border-box;margin:0;padding:0}
html,body{width:1200px;height:4383px;overflow:hidden}
body{font-family:"Work Sans",Arial,sans-serif;color:var(--text);background:var(--white);font-size:13px;line-height:1.45}
.head{font-family:"Lexend",Arial,sans-serif;color:var(--ink);font-weight:500;letter-spacing:.2px}
a{color:inherit;text-decoration:none}
section,header,footer{position:relative;width:1200px}
.abs{position:absolute}
svg{display:block}

/* top bar */
.topbar{height:31px}
.topbar-strip{position:absolute;left:439px;top:0;width:599px;height:31px;background:var(--teal);clip-path:polygon(12px 0,100% 0,calc(100% - 12px) 100%,0 100%);display:flex;align-items:center;color:#fff;font-size:11.5px;padding-left:40px;gap:40px}
.topbar-strip span{display:flex;align-items:center;gap:5px}
.topbar-strip .lang{margin-left:auto;margin-right:40px}
.topbar-line{position:absolute;left:0;top:0;width:1200px;height:3px;background:var(--teal)}

/* header */
.site-header{height:73px}
.brand{position:absolute;display:flex;align-items:center;gap:8px;font-family:"Work Sans",sans-serif;font-weight:500;color:var(--teal);font-size:15px}
.brand .mark{width:22px;height:22px;border:2px solid var(--teal);border-radius:3px}
.nav{position:absolute;left:446px;top:28px;display:flex;gap:28px;font-size:14px;color:var(--ink);font-weight:500}
.nav .active{color:var(--teal)}
.call{position:absolute;display:flex;align-items:center;gap:8px}
.call .ring{width:28px;height:28px;border:1.5px solid var(--teal);border-radius:50%;display:flex;align-items:center;justify-content:center}
.call small{display:block;font-size:12px;color:var(--ink);line-height:1.1}
.call b{display:block;font-size:17px;color:var(--teal);font-weight:500;line-height:1.2}

/* buttons */
.btn-line{position:absolute;border:1.5px solid var(--navy);color:var(--navy);font-weight:600;font-size:12.5px;display:flex;align-items:center;justify-content:center;background:transparent}
.btn-line::after{content:"";position:absolute;right:-22px;top:50%;width:32px;height:1.5px;background:currentColor}
.btn-line.teal{border-color:var(--teal);color:var(--teal)}
.btn-line.light{border-color:#fff;color:#fff}

/* hero */
.hero{height:480px;background:linear-gradient(100deg,#3f6f82 0%,#2f6477 35%,#1d4a5e 60%,#26506a 100%)}
.hero-photo{position:absolute;inset:0;background:radial-gradient(ellipse at 70% 40%,rgba(140,180,195,.35),transparent 60%),radial-gradient(ellipse at 30% 80%,rgba(20,60,80,.4),transparent 60%)}
.hero h1{position:absolute;left:158px;top:122px;font-size:48px;line-height:43px;color:#fff;font-weight:500}

/* about */
.about{height:636px}
.sec-title{text-align:center;font-size:36px;line-height:37px}
.sec-lead{text-align:center;font-size:13px;line-height:21px;color:var(--text)}
.card{position:absolute;top:235px;width:273px;height:356px}
.card .photo{width:273px;height:308px}
.card .box{position:absolute;left:20px;top:179px;width:232px;height:177px;background:#fff;box-shadow:0 10px 30px rgba(0,0,0,.08);padding:20px 26px}
.card .box h3{font-size:16px;margin-bottom:8px}
.card .box p{font-size:12.5px;line-height:18px}
.learn{display:inline-block;margin-top:12px;font-size:12px;font-weight:600;letter-spacing:1px;color:var(--teal);border-bottom:1.5px solid var(--teal);line-height:15px}
.card.featured .box{background:var(--teal);color:#eafafc}
.card.featured .box h3,.card.featured .learn{color:#fff;border-color:#fff}

/* consulting */
.consult{height:559px}
.consult-photo{position:absolute;left:158px;top:77px;width:429px;height:374px;border-radius:28px 28px 28px 28px;background:linear-gradient(135deg,#c9d5dc,#8ea6b2 55%,#5e7784)}
.eyebrow{font-size:12px;color:var(--text)}
.checks{display:grid;grid-template-columns:210px 200px;row-gap:8px;font-size:12px;color:var(--navy);font-weight:600}
.checks span{display:flex;align-items:center;gap:6px}

/* mission */
.mission{height:267px;background:linear-gradient(90deg,#eef1f3,#f6f7f8 50%,#eef1f3)}

/* services */
.services{height:485px}
.svc{position:absolute;top:214px;width:270px}
.svc h4{font-family:"Work Sans",sans-serif;font-weight:600;font-size:15.5px;color:var(--navy);margin:24px 0 10px}
.svc p{font-size:12.5px;line-height:18px}

/* stats */
.stats{height:179px;background:linear-gradient(90deg,#108a98 0%,#0c5e78 45%,#0b3553 100%)}
.stat{position:absolute;top:58px;width:300px;text-align:center;color:#fff}
.stat b{display:block;font-family:"Lexend",sans-serif;font-weight:500;font-size:36px;line-height:40px}
.stat span{font-size:11.5px;font-weight:600;letter-spacing:.8px}

/* testimonial */
.testi{height:370px}
.testi-photo{position:absolute;left:0;top:0;width:347px;height:337px;background:linear-gradient(120deg,#dde4e8,#eff2f3 60%,#e2e8ea)}
.avatar-ring{position:absolute;left:405px;top:163px;width:126px;height:126px;border:2px solid var(--teal);border-radius:50%;display:flex;align-items:center;justify-content:center}
.avatar{width:104px;height:104px;border-radius:50%;background:linear-gradient(160deg,#d9c2ae,#b99a84)}
.quote{position:absolute;left:548px;top:176px;width:432px;font-style:italic;font-size:12.5px;line-height:19px}
.dots{position:absolute;left:419px;top:326px;display:flex;gap:10px}
.dots i{width:9px;height:9px;border-radius:50%;background:#d7e3e6}
.dots i.on{background:var(--teal)}

/* news */
.news{height:620px}
.post{position:absolute;top:169px;width:274px}
.post .photo{height:223px}
.post h3{font-size:19px;line-height:24px;margin-top:28px}
.post .meta{display:flex;gap:14px;font-size:11.5px;color:var(--teal);margin-top:6px}
.post .meta span{display:flex;align-items:center;gap:4px}
.post p{font-size:12.5px;line-height:18px;margin-top:16px}

/* partners */
.partners{height:177px}
.partners::before{content:"";position:absolute;left:0;top:36px;width:1200px;height:1px;background:var(--line)}
.badge{position:absolute;top:90px;display:flex;align-items:center;gap:6px;opacity:.35}
.badge.on{opacity:.85}
.badge i{width:28px;height:28px;border-radius:50%;background:#9aa3aa}
.badge s{width:82px;height:16px;border-radius:4px;background:#b9c0c5;text-decoration:none}
.badge.on i,.badge.on s{background:#4c5560}

/* footer */
.site-footer{height:446px;background:var(--navy);color:#cfdbe4}
.site-footer h5{font-family:"Work Sans",sans-serif;font-size:13px;font-weight:600;letter-spacing:.5px;color:#fff}
.flinks{list-style:none;font-size:12.5px;line-height:25px;margin-top:16px}
.subscribe{position:absolute;left:158px;top:234px;width:305px;height:136px;background:var(--navy-deep);padding:28px 26px}
.subscribe p{color:#fff;font-size:12.5px;line-height:15px}
.field{display:flex;margin-top:14px;height:35px}
.field span{flex:1;border:1px solid #3f6580;font-size:11px;color:#cfdbe4;display:flex;align-items:center;padding-left:10px}
.field b{width:56px;background:var(--teal);color:#fff;font-size:12px;display:flex;align-items:center;justify-content:center}
.socials{position:absolute;left:505px;top:332px;display:flex;gap:18px}
.socials i{width:25px;height:25px;border:1.5px solid #cfdbe4;border-radius:50%}
.contact-row{position:absolute;left:826px;display:flex;gap:10px;align-items:flex-start;font-size:12px}
.contact-row .dot{width:34px;height:34px;border-radius:50%;background:#fff;display:flex;align-items:center;justify-content:center;flex:none}
.contact-row b{color:#fff;display:block;font-weight:600}
.bottombar{height:60px;background:var(--navy-deep);color:#aebdca;font-size:11px}
</style>
</head>
<body>

<!-- top bar -->
<div class="topbar" style="position:relative;height:31px">
  <div class="topbar-strip">
    <span><svg width="13" height="10" viewBox="0 0 13 10"><rect x=".5" y=".5" width="12" height="9" fill="none" stroke="#fff"/><path d="M.5 .5l6 5 6-5" fill="none" stroke="#fff"/></svg>contact@dubreuil-conseil.com</span>
    <span><svg width="9" height="12" viewBox="0 0 9 12"><path d="M4.5 11.5S.5 7 .5 4.5a4 4 0 0 1 8 0C8.5 7 4.5 11.5 4.5 11.5z" fill="#fff"/><circle cx="4.5" cy="4.5" r="1.5" fill="#0f8a98"/></svg>27 Rue des Tanneurs, Lyon</span>
    <span class="lang"><svg width="11" height="11" viewBox="0 0 11 11"><circle cx="5.5" cy="5.5" r="5" fill="none" stroke="#fff"/><path d="M.5 5.5h10M5.5.5c-2.5 3-2.5 7 0 10M5.5.5c2.5 3 2.5 7 0 10" fill="none" stroke="#fff" stroke-width=".8"/></svg>EN ⌄</span>
  </div>
</div>

<header class="site-header">
  <div class="brand" style="left:158px;top:22px"><span class="mark"></span>Laurent Dubreuil Conseil</div>
  <nav class="nav"><a class="active">Home</a><a>About</a><a>Services</a><a>Pages</a><a>Blog</a><a>Contact</a></nav>
  <div class="call" style="left:900px;top:18px">
    <span class="ring"><svg width="13" height="13" viewBox="0 0 24 24"><path d="M6.6 10.8a15 15 0 0 0 6.6 6.6l2.2-2.2a1 1 0 0 1 1-.25 11.4 11.4 0 0 0 3.6.57 1 1 0 0 1 1 1V20a1 1 0 0 1-1 1A17 17 0 0 1 3 4a1 1 0 0 1 1-1h3.5a1 1 0 0 1 1 1c0 1.25.2 2.45.57 3.57a1 1 0 0 1-.25 1z" fill="#0f8a98"/></svg></span>
    <div><small>Call Anytime</small><b>(38) 512-940</b></div>
  </div>
</header>

<!-- hero -->
<section class="hero">
  <div class="hero-photo" role="img" aria-label="Photo of two consultants in suits reviewing work on a laptop, teal tinted"></div>
  <h1 class="head">The Fastest<br>way to achieve<br>success</h1>
  <a class="btn-line light" style="left:158px;top:282px;width:170px;height:38px">Free Consultation</a>
</section>

<!-- about -->
<section class="about">
  <h2 class="head sec-title abs" style="left:0;top:68px;width:1200px">About<br>Laurent Dubreuil Conseil</h2>
  <p class="sec-lead abs" style="left:0;top:158px;width:1200px">Lorem ipsum dolor sit amet, consectetur adipiscing elit, sed do eiusmod tempor incididunt<br>ut labore et dolore magna aliqua. Ut enim ad minim veniam,</p>

  <article class="card" style="left:158px">
    <div class="photo" role="img" aria-label="Photo of a brass combination padlock" style="background:linear-gradient(140deg,#e9e2d2,#c9a45b 50%,#8a6a2e)"></div>
    <div class="box"><h3 class="head">Sed ut Perspiciatis</h3><p>Lorem ipsum dolor sit amet, consectetur adipisc ing elit, sed do eiusmod tempor incidi..</p><a class="learn">LEARN MORE</a></div>
  </article>
  <article class="card featured" style="left:463px">
    <div class="photo" role="img" aria-label="Photo of team members stacking hands together" style="background:linear-gradient(140deg,#2f5d86,#c99b83 55%,#e8ddd3)"></div>
    <div class="box"><h3 class="head">Ut enim ad minim</h3><p>Lorem ipsum dolor sit amet, consectetur adipisc ing elit, sed do eiusmod tempor incidi..</p><a class="learn">LEARN MORE</a></div>
  </article>
  <article class="card" style="left:769px">
    <div class="photo" role="img" aria-label="Photo of a laptop and headphones on an office desk" style="background:linear-gradient(140deg,#f2f3f4,#c8ccd0 55%,#4a4e54)"></div>
    <div class="box"><h3 class="head">Duis aute irure dolor</h3><p>Lorem ipsum dolor sit amet, consectetur adipisc ing elit, sed do eiusmod tempor incidi..</p><a class="learn">LEARN MORE</a></div>
  </article>
</section>

<!-- consulting -->
<section class="consult">
  <div class="consult-photo" role="img" aria-label="Photo of a consultant and a colleague looking at a laptop"></div>
  <p class="eyebrow abs" style="left:640px;top:104px">General presentation</p>
  <h2 class="head abs" style="left:640px;top:121px;font-size:34px;line-height:37px">Consulting Market<br>Leader Expert</h2>
  <svg class="abs" style="left:640px;top:216px" width="62" height="66" viewBox="0 0 62 66" fill="none" stroke="#0f8a98" stroke-width="2"><rect x="2" y="2" width="36" height="50" rx="2"/><path d="M9 14h22M9 22h22M9 30h14M9 38h10"/><circle cx="42" cy="42" r="12"/><path d="M36 42l4 4 8-8M50 51l9 9"/></svg>
  <p class="abs" style="left:716px;top:222px;width:310px;font-size:12.5px;line-height:18px;color:var(--ink)">Lorem ipsum dolor sit amet, consectetur adipiscing elit, sed do eiusmod tempor incidid ut labore et dolore mag...</p>
  <div class="checks abs" style="left:640px;top:312px">
    <span><svg width="12" height="12" viewBox="0 0 12 12"><rect x=".75" y=".75" width="10.5" height="10.5" rx="2" fill="none" stroke="#0c3350" stroke-width="1.3"/><path d="M3 6l2 2 4-4" fill="none" stroke="#0c3350" stroke-width="1.4"/></svg>Sed ut perspic unde omnis</span>
    <span><svg width="12" height="12" viewBox="0 0 12 12"><rect x=".75" y=".75" width="10.5" height="10.5" rx="2" fill="none" stroke="#0c3350" stroke-width="1.3"/><path d="M3 6l2 2 4-4" fill="none" stroke="#0c3350" stroke-width="1.4"/></svg>Sed ut perspic unde omnis</span>
    <span><svg width="12" height="12" viewBox="0 0 12 12"><rect x=".75" y=".75" width="10.5" height="10.5" rx="2" fill="none" stroke="#0c3350" stroke-width="1.3"/><path d="M3 6l2 2 4-4" fill="none" stroke="#0c3350" stroke-width="1.4"/></svg>Pste natus eor sit volup</span>
    <span><svg width="12" height="12" viewBox="0 0 12 12"><rect x=".75" y=".75" width="10.5" height="10.5" rx="2" fill="none" stroke="#0c3350" stroke-width="1.3"/><path d="M3 6l2 2 4-4" fill="none" stroke="#0c3350" stroke-width="1.4"/></svg>Pste natus eor sit volup</span>
  </div>
  <a class="btn-line teal" style="left:640px;top:383px;width:153px;height:41px">Find Out More</a>
  <div class="call" style="left:818px;top:386px">
    <span class="ring"><svg width="13" height="13" viewBox="0 0 24 24"><path d="M6.6 10.8a15 15 0 0 0 6.6 6.6l2.2-2.2a1 1 0 0 1 1-.25 11.4 11.4 0 0 0 3.6.57 1 1 0 0 1 1 1V20a1 1 0 0 1-1 1A17 17 0 0 1 3 4a1 1 0 0 1 1-1h3.5a1 1 0 0 1 1 1c0 1.25.2 2.45.57 3.57a1 1 0 0 1-.25 1z" fill="#0f8a98"/></svg></span>
    <div><small>Call Anytime</small><b>(38) 512-940</b></div>
  </div>
</section>

<!-- mission -->
<section class="mission" role="img" aria-label="Faded photo of a team meeting in an office">
  <h2 class="head sec-title abs" style="left:0;top:66px;width:1200px;color:var(--navy)">Our Mission is to Protect your<br>Business &amp; Much More</h2>
  <a class="btn-line" style="left:519px;top:165px;width:170px;height:40px">Free Consultation</a>
</section>

<!-- services -->
<section class="services">
  <h2 class="head abs" style="left:158px;top:88px;font-size:34px">Services We Provide</h2>
  <p class="abs" style="left:158px;top:140px;width:620px;font-size:13px;line-height:21px">Lorem ipsum dolor sit amet, consectetur adipiscing elit, sed do eiusmod tempor incididunt ut labore et dolore magna aliqua. Ut enim ad minim veniam,</p>
  <a class="btn-line" style="left:875px;top:119px;width:167px;height:40px">More Services</a>

  <div class="svc" style="left:158px">
    <svg width="70" height="66" viewBox="0 0 70 66" fill="none" stroke="#0c3350" stroke-width="2"><path d="M4 40l14-14 14 14M10 34v20h16V34"/><path d="M2 58h30"/><circle cx="48" cy="46" r="14"/><path d="M48 38v16M44 42h6a2 2 0 0 1 0 4h-4a2 2 0 0 0 0 4h6"/><circle cx="40" cy="10" r="3"/><circle cx="50" cy="18" r="2"/></svg>
    <h4>Industrial Goods &amp; Services</h4>
    <p>Sed ut perspiciatis unde omnis iste natus error sit volup tatem accusantium doloremque laudantium,</p>
    <a class="learn">LEARN MORE</a>
  </div>
  <div class="svc" style="left:470px">
    <svg width="70" height="66" viewBox="0 0 70 66" fill="none" stroke="#0c3350" stroke-width="2"><circle cx="24" cy="22" r="15"/><path d="M18 37v8h12v-8M19 50h10M24 14v16M20 18h6a2 2 0 0 1 0 4h-4a2 2 0 0 0 0 4h6"/><path d="M44 62V50h6v12M54 62V42h6v20M34 62h30"/></svg>
    <h4>Startup Business Planning</h4>
    <p>Sed ut perspiciatis unde omnis iste natus error sit volup tatem accusantium doloremque laudantium,</p>
    <a class="learn">LEARN MORE</a>
  </div>
  <div class="svc" style="left:783px">
    <svg width="70" height="66" viewBox="0 0 70 66" fill="none" stroke="#0c3350" stroke-width="2"><circle cx="30" cy="36" r="22" stroke-dasharray="6 4"/><circle cx="30" cy="36" r="13"/><path d="M36 6v24h24A24 24 0 0 0 36 6z"/></svg>
    <h4>Social &amp; Public Sector service</h4>
    <p>Sed ut perspiciatis unde omnis iste natus error sit volup tatem accusantium doloremque laudantium,</p>
    <a class="learn">LEARN MORE</a>
  </div>
</section>

<!-- stats -->
<section class="stats">
  <div class="stat" style="left:136px"><b>500+</b><span>SUCCESSFULLY COMPLETED CASES</span></div>
  <div class="stat" style="left:454px"><b>750+</b><span>HIGHLY&nbsp; SPECIALISED CONSULTANTS</span></div>
  <div class="stat" style="left:771px"><b>100%</b><span>SATISFACTION OF OUR CUSTOMERS</span></div>
</section>

<!-- testimonials -->
<section class="testi">
  <div class="testi-photo" role="img" aria-label="Faded photo of hands writing in a notebook on a desk"></div>
  <h2 class="head abs" style="left:408px;top:104px;font-size:34px">What They’re Saying</h2>
  <svg class="abs" style="left:872px;top:160px" width="110" height="80" viewBox="0 0 110 80"><path d="M0 40c0-22 12-36 34-40v14c-10 3-14 10-14 18h14v40H0zM58 40c0-22 12-36 34-40v14c-10 3-14 10-14 18h14v40H58z" fill="#eef1f2" transform="rotate(180 55 40)"/></svg>
  <div class="avatar-ring"><div class="avatar" role="img" aria-label="Client portrait photo"></div></div>
  <p class="quote">Lorem ipsum dolor sit amet, consectetur adipiscing elit, sed do eius mod tempor incididunt ut labore et dolore magna aliqua.<br>Ut enim ad minim veniam, quis nostrud exercitation ullamco laboris nisi ut aliquip ex ea commodo consequat</p>
  <p class="abs" style="left:548px;top:270px;font-size:13px;font-weight:600;letter-spacing:1px;color:var(--teal)">CLIENTS NAME</p>
  <div class="dots"><i></i><i class="on"></i><i></i></div>
</section>

<!-- news -->
<section class="news">
  <h2 class="head sec-title abs" style="left:0;top:76px;width:1200px">News &amp; Articles</h2>
  <p class="sec-lead abs" style="left:0;top:113px;width:1200px">Lorem ipsum dolor sit amet, consectetur adipiscing elit, sed do eiusmod tempor incididunt<br>ut labore et dolore magna aliqua. Ut enim ad minim veniam,</p>

  <article class="post" style="left:150px">
    <div class="photo" role="img" aria-label="Overhead photo of a team working on laptops at a table" style="background:linear-gradient(135deg,#c9b9a4,#8c8a86 50%,#3d4247)"></div>
    <h3 class="head">Sed ut perspiciatis de omnis iste nat</h3>
    <div class="meta"><span>◷ April 19, 2017</span><span>● 0 comment</span></div>
    <p>Lorem ipsum dolor sit amet, consectetur adipiscing elit, sed do eiusmod tempor inc ididunt ut labore et dolore magna aliqua. Ut enim ad minim veniam...</p>
  </article>
  <article class="post" style="left:463px">
    <div class="photo" role="img" aria-label="Photo looking up at glass office towers against a blue sky" style="background:linear-gradient(160deg,#9fbbe0,#36538a 55%,#1a2744)"></div>
    <h3 class="head">Sed ut perspiciatis de omnis iste nat</h3>
    <div class="meta"><span>◷ April 19, 2017</span><span>● 0 comment</span></div>
    <p>Lorem ipsum dolor sit amet, consectetur adipiscing elit, sed do eiusmod tempor inc ididunt ut labore et dolore magna aliqua. Ut enim ad minim veniam...</p>
  </article>
  <article class="post" style="left:776px">
    <div class="photo" role="img" aria-label="Photo of a person reviewing charts on a tablet" style="background:linear-gradient(135deg,#e8ecef,#b7c4d3 50%,#3a4b6a)"></div>
    <h3 class="head">Sed ut perspiciatis de omnis iste nat</h3>
    <div class="meta"><span>◷ April 19, 2017</span><span>● 0 comment</span></div>
    <p>Lorem ipsum dolor sit amet, consectetur adipiscing elit, sed do eiusmod tempor inc ididunt ut labore et dolore magna aliqua. Ut enim ad minim veniam...</p>
  </article>
</section>

<!-- partners -->
<section class="partners">
  <div class="badge" style="left:80px"><i></i><s></s></div>
  <div class="badge" style="left:259px"><i></i><s></s></div>
  <div class="badge" style="left:446px"><i></i><s></s></div>
  <div class="badge on" style="left:632px"><i></i><s></s></div>
  <div class="badge" style="left:812px"><i></i><s></s></div>
  <div class="badge" style="left:998px"><i></i><s></s></div>
</section>

<!-- footer -->
<footer class="site-footer">
  <div class="brand" style="left:228px;top:100px;color:#fff"><span class="mark" style="border-color:#fff"></span>Laurent Dubreuil Conseil</div>
  <p class="abs" style="left:158px;top:176px;width:305px;font-size:12.5px;line-height:18px;color:#fff">Lorem ipsum dolor sit amet, consectetur adipi scing elit, sed do eiusmod tem...</p>
  <div class="subscribe">
    <p>Subscribe for Latest News<br>and Resources</p>
    <div class="field"><span>Email Address</span><b>GO</b></div>
  </div>

  <div class="abs" style="left:505px;top:90px"><h5>OUR PROJECTS</h5><ul class="flinks"><li>About</li><li>Meet our Team</li><li>Latest News</li><li>Events</li><li>Contact</li></ul></div>
  <div class="abs" style="left:684px;top:90px"><h5>COMPANY</h5><ul class="flinks"><li>Overview</li><li>Services</li><li>Portfolio</li><li>Our Partner</li><li>Our Awards</li></ul></div>
  <h5 class="abs" style="left:826px;top:90px">CONTACT</h5>
  <div class="contact-row" style="top:130px">
    <span class="dot"><svg width="15" height="11" viewBox="0 0 15 11"><rect x=".5" y=".5" width="14" height="10" fill="none" stroke="#0f8a98"/><path d="M.5 .5l7 5.5 7-5.5" fill="none" stroke="#0f8a98"/></svg></span>
    <div>Email Address<b>contact@dubreuil-conseil.com</b></div>
  </div>
  <div class="contact-row" style="top:182px">
    <span class="dot"><svg width="11" height="15" viewBox="0 0 9 12"><path d="M4.5 11.5S.5 7 .5 4.5a4 4 0 0 1 8 0C8.5 7 4.5 11.5 4.5 11.5z" fill="#0f8a98"/><circle cx="4.5" cy="4.5" r="1.5" fill="#fff"/></svg></span>
    <div>Locations<b style="width:180px">123, Lorem ipsum dolor sit amet, consectetur</b></div>
  </div>

  <div class="abs" style="left:505px;top:307px;width:537px;height:1px;background:#2b516c"></div>
  <div class="socials"><i></i><i></i><i></i><i></i><i></i></div>
  <div class="call" style="left:829px;top:330px">
    <span class="ring" style="width:24px;height:24px;border-color:#cfdbe4"><svg width="11" height="11" viewBox="0 0 24 24"><path d="M6.6 10.8a15 15 0 0 0 6.6 6.6l2.2-2.2a1 1 0 0 1 1-.25 11.4 11.4 0 0 0 3.6.57 1 1 0 0 1 1 1V20a1 1 0 0 1-1 1A17 17 0 0 1 3 4a1 1 0 0 1 1-1h3.5a1 1 0 0 1 1 1c0 1.25.2 2.45.57 3.57a1 1 0 0 1-.25 1z" fill="#cfdbe4"/></svg></span>
    <div><small style="color:#fff">Call Anytime</small><b style="color:#fff">(38) 512-940</b></div>
  </div>
</footer>

<div class="bottombar" style="position:relative">
  <span class="abs" style="left:158px;top:24px">© Copyright 2022 Laurent Dubreuil Conseil. All rights reserved.</span>
  <span class="abs" style="left:846px;top:24px">Legal</span>
  <span class="abs" style="left:900px;top:24px">Sitemap</span>
  <span class="abs" style="left:973px;top:24px">Privacy Policy</span>
</div>

</body>
</html>
```